Biz card p jester

I am a children's entertainer for birthdays, functions, events,festivals doing crazy silliness , balloon twisting ,mad magic , fantastic Facepainting and airbrush tattoos . High energy act focused on fun more than skill.
Very popular with under 5s
My makeup is a rainbow across my eyes
Want a card that kids love and pass on to parents
Like the colours magenta brite blue and yellow
Maybe 'Pip the Jester ' in a circle
Updates
like the colours hot pink, blue and yellow
thinking "Pip the Jester" inside a shape
Target Market(s)
Parents,event organisers,kids
Industry/Entity Type
Events
Contact Information for Business Card
Pip the Jester
Entertainment
0412657391
Pipthejester.com.au
Pipthejester@fizzmail.example
Look and feel
Each slider illustrates characteristics of the customer's brand and the style your logo design should communicate.

```html
<!DOCTYPE html>
<html lang="en">
<head>
<meta charset="utf-8">
<title>Pip the Jester – Business Card</title>
<link href="https://fonts.googleapis.com/css2?family=Marcellus&family=Fredoka:wght@600&display=swap" rel="stylesheet">
<style>
  :root {
    --page-bg: #ececec;
    --sky-blue: #14a8e4;
    --sky-blue-light: #3cc0f0;
    --sunny-yellow: #f1ea3a;
    --hot-pink: #e8197f;
    --brite-blue: #1267b0;
    --party-orange: #f58a1f;
    --lime: #9cd13a;
    --purple: #7b3fa0;
  }
  * { margin: 0; padding: 0; box-sizing: border-box; }
  html, body { width: 1200px; height: 1044px; overflow: hidden; }
  body { background: var(--page-bg); position: relative; font-family: "Marcellus", serif; }

  .card { position: absolute; width: 700px; height: 432px; overflow: hidden; }
  .card--front { left: 57px; top: 44px; background: linear-gradient(90deg, var(--sky-blue-light), var(--sky-blue)); }
  .card--back { left: 438px; top: 548px; background: var(--sunny-yellow); }

  .stripe-band {
    position: absolute; left: 0; width: 100%;
    background: linear-gradient(90deg, var(--hot-pink), var(--party-orange), var(--sunny-yellow), var(--lime), var(--sky-blue), var(--purple), var(--hot-pink));
  }
  .card--front .stripe-band { top: 0; height: 30px; }
  .card--back .stripe-band { bottom: 0; height: 52px; }

  .bunting {
    position: absolute; left: 0; top: 30px; width: 100%; height: 68px;
    background: linear-gradient(180deg, rgba(245,138,31,.85), rgba(232,25,127,.35));
  }
  .wave { position: absolute; left: 0; bottom: 0; width: 100%; height: 90px; }

  .balloons {
    position: absolute;
    background: radial-gradient(circle at 40% 40%, #ffd23a, var(--party-orange) 45%, var(--hot-pink) 80%, transparent 82%);
  }
  .card--front .balloons { left: 0; top: 250px; width: 270px; height: 182px;
    background: linear-gradient(120deg, #ffd23a, var(--party-orange) 45%, var(--lime) 70%, var(--hot-pink)); border-top-right-radius: 140px; }
  .card--back .balloons--top { left: 0; top: 0; width: 260px; height: 140px;
    background: linear-gradient(120deg, var(--lime), var(--party-orange) 45%, var(--hot-pink) 80%, rgba(241,234,58,0)); border-bottom-right-radius: 140px; }

  .performer-photo { position: absolute; }
  .card--front .performer-photo { left: 470px; top: 32px; width: 206px; height: 378px;
    background: linear-gradient(180deg, var(--purple), #c0304f 35%, #3a2a6a 70%, var(--hot-pink)); border-radius: 40px 40px 6px 6px; opacity: .9; }
  .card--back .performer-photo { left: 470px; top: 150px; width: 230px; height: 230px;
    background: linear-gradient(160deg, var(--purple), #f4e6dc 45%, var(--party-orange) 75%, var(--lime)); border-radius: 50% 50% 0 0; }

  .brand-name { position: absolute; font-family: "Fredoka", sans-serif; font-weight: 600; color: var(--hot-pink); white-space: nowrap; }
  .card--front .brand-name { left: 38px; top: 130px; font-size: 66px; }
  .card--back .brand-name { left: 390px; top: 46px; font-size: 38px; }

  .contact-block { position: absolute; left: 44px; top: 155px; }
  .contact-block__name { color: var(--hot-pink); font-size: 27px; line-height: 1.2; }
  .contact-block__role { color: var(--brite-blue); font-size: 18px; font-weight: bold; margin-bottom: 30px; }
  .contact-list { list-style: none; }
  .contact-list li { display: flex; align-items: center; gap: 10px; color: var(--brite-blue); font-size: 19px; font-weight: bold; height: 30px; }
  .contact-list svg { width: 18px; height: 18px; flex: none; }
</style>
</head>
<body>

<section class="card card--front">
  <div class="stripe-band" role="img" aria-label="Multicoloured vertical stripe border"></div>
  <div class="bunting" role="img" aria-label="Row of colourful party bunting flags"></div>
  <svg class="wave" viewBox="0 0 700 90" preserveAspectRatio="none">
    <path d="M0 70 C200 20 400 30 700 40 L700 90 L0 90 Z" fill="var(--hot-pink)"/>
    <path d="M0 82 C220 45 420 50 700 58 L700 90 L0 90 Z" fill="var(--sunny-yellow)"/>
  </svg>
  <div class="balloons" role="img" aria-label="Cluster of party balloons with stars and streamers"></div>
  <div class="brand-name">Pip the Jester</div>
  <div class="performer-photo" role="img" aria-label="Photo of the entertainer in full costume standing on stage"></div>
</section>

<section class="card card--back">
  <div class="balloons balloons--top" role="img" aria-label="Cluster of party balloons with confetti"></div>
  <div class="brand-name">Pip the Jester</div>
  <div class="contact-block">
    <p class="contact-block__name">Pip the Jester</p>
    <p class="contact-block__role">Clown for childrens entertainment</p>
    <ul class="contact-list">
      <li>
        <svg viewBox="0 0 24 24"><path d="M6 2 L10 6 L8 9 C9 12 12 15 15 16 L18 14 L22 18 L19 22 C10 21 3 14 2 5 Z" fill="var(--hot-pink)"/></svg>
        0412657391
      </li>
      <li>
        <svg viewBox="0 0 24 24" fill="none" stroke="var(--hot-pink)" stroke-width="2.2"><circle cx="12" cy="12" r="10"/><ellipse cx="12" cy="12" rx="4.5" ry="10"/><path d="M2 12 H22 M4 7 H20 M4 17 H20"/></svg>
        Pipthejester.com.au
      </li>
      <li>
        <svg viewBox="0 0 24 24"><rect x="2" y="5" width="20" height="14" fill="var(--hot-pink)"/><path d="M2 5 L12 13 L22 5" fill="none" stroke="#fff" stroke-width="1.8"/></svg>
        Pipthejester@fizzmail.example
      </li>
    </ul>
  </div>
  <div class="performer-photo" role="img" aria-label="Portrait photo of the entertainer in rainbow face paint surrounded by balloons"></div>
  <div class="stripe-band" role="img" aria-label="Multicoloured vertical stripe border"></div>
</section>

</body>
</html>
```